Lagoonworks Solutions

I run an aquarium service business covering all aspects of large scale saltwater aquariums. Design, installation, and service. My main customer base is corporations in Manhattan, but I also deal with smaller home or business aquariums in the tri-state area. I work with cutting edge equipment and service techniques and need to convey that.

Industry/Entity Type

Business

Contact Information for Business Card

LAGOONWORKS SOLUTIONS LLC
Jonathan R. Delvoy
Owner
Main 415-555-0182
Cell 415-555-0267
Service.LagoonSolutions@mailbeam.net

```html
<!DOCTYPE html>
<html lang="en">
<head>
<meta charset="utf-8">
<title>Lagoonworks Solutions — Business Card</title>
<link href="https://fonts.googleapis.com/css2?family=Didact+Gothic&display=swap" rel="stylesheet">
<style>
  :root {
    --backdrop: #3d4749;
    --card-white: #ffffff;
    --card-mist: #eef0f1;
    --accent-stripe: #4fe0e8;
    --ink: #1e2224;
    --brand-blue: #2f93cf;
    --icon-blue: #2f6fe0;
    --contact-ink: #3a3f42;
    --art-deep: #2c3336;
    --art-steel: #9aa6ab;
    --bubble-blue: #4fb6f0;
    --bubble-aqua: #5ee0ea;
  }
  html, body {
    margin: 0;
    padding: 0;
    width: 1200px;
    height: 741px;
    overflow: hidden;
    background: var(--backdrop);
  }
  .business-card {
    position: absolute;
    left: 100px;
    top: 85px;
    width: 1000px;
    height: 571px;
    overflow: hidden;
    background: linear-gradient(90deg, var(--card-white) 0, var(--card-white) 277px, var(--card-mist) 277px, var(--card-white) 100%);
    font-family: "Didact Gothic", "Century Gothic", sans-serif;
  }
  .accent-stripe {
    position: absolute;
    left: 0;
    top: 0;
    width: 10px;
    height: 100%;
    background: var(--accent-stripe);
  }
  .mascot-art {
    position: absolute;
    left: 55px;
    top: 90px;
    width: 164px;
    height: 370px;
    border-radius: 40% 40% 45% 45% / 20% 20% 30% 30%;
    background: radial-gradient(ellipse at 50% 45%, var(--art-steel) 0%, #5d686c 45%, var(--art-deep) 100%);
  }
  .bubble-field {
    position: absolute;
    right: 0;
    top: 0;
    width: 200px;
    height: 100%;
    background: linear-gradient(90deg, rgba(79, 182, 240, 0) 0%, rgba(79, 182, 240, 0.55) 45%, var(--bubble-blue) 75%, var(--bubble-aqua) 100%);
  }
  .holder-name {
    position: absolute;
    left: 308px;
    top: 92px;
    margin: 0;
    font-size: 58px;
    font-weight: 400;
    letter-spacing: 2px;
    line-height: 1;
    color: var(--ink);
    white-space: nowrap;
  }
  .company-name {
    position: absolute;
    left: 313px;
    top: 166px;
    margin: 0;
    font-size: 40px;
    letter-spacing: 3px;
    line-height: 1;
    color: var(--brand-blue);
    white-space: nowrap;
  }
  .holder-title {
    position: absolute;
    left: 315px;
    top: 222px;
    margin: 0;
    font-size: 24px;
    letter-spacing: 2px;
    line-height: 1;
    color: var(--contact-ink);
  }
  .contact-list {
    position: absolute;
    left: 333px;
    top: 330px;
    margin: 0;
    padding: 0;
    list-style: none;
    font-size: 27px;
    letter-spacing: 1px;
    color: var(--contact-ink);
  }
  .contact-list li {
    display: flex;
    align-items: center;
    height: 44px;
    white-space: nowrap;
  }
  .contact-icon {
    width: 22px;
    height: 22px;
    margin-right: 40px;
    fill: var(--icon-blue);
  }
</style>
</head>
<body>
  <section class="business-card">
    <div class="accent-stripe"></div>
    <div class="mascot-art" role="img" aria-label="Metallic seahorse illustration with small bubbles"></div>
    <div class="bubble-field" role="img" aria-label="Decorative cluster of blue and aqua bubbles"></div>

    <h1 class="holder-name">Jonathan R. Delvoy</h1>
    <p class="company-name">Lagoonworks Solutions LLC</p>
    <p class="holder-title">Owner</p>

    <ul class="contact-list">
      <li>
        <svg class="contact-icon" viewBox="0 0 24 24" aria-hidden="true"><path d="M6.6 10.8a15.1 15.1 0 0 0 6.6 6.6l2.2-2.2a1 1 0 0 1 1-.25 11.4 11.4 0 0 0 3.6.57 1 1 0 0 1 1 1V20a1 1 0 0 1-1 1A17 17 0 0 1 3 4a1 1 0 0 1 1-1h3.5a1 1 0 0 1 1 1c0 1.25.2 2.45.57 3.57a1 1 0 0 1-.25 1z"/></svg>
        415-555-0182
      </li>
      <li>
        <svg class="contact-icon" viewBox="0 0 24 24" aria-hidden="true"><path d="M7 1h10a2 2 0 0 1 2 2v18a2 2 0 0 1-2 2H7a2 2 0 0 1-2-2V3a2 2 0 0 1 2-2zm0 3v14h10V4zm5 15.5a1 1 0 1 0 0 2 1 1 0 0 0 0-2z"/></svg>
        415-555-0267
      </li>
      <li>
        <svg class="contact-icon" viewBox="0 0 24 24" aria-hidden="true"><path d="M2 5h20v14H2zm2 2v.5l8 5 8-5V7zm0 2.8V17h16V9.8l-8 5z"/></svg>
        Service.LagoonSolutions@mailbeam.net
      </li>
    </ul>
  </section>
</body>
</html>
```